business card deign

Logo needs the following on it.
1. attached logo
2. Tagline - "If it keeps a drink cold or the party going...we do it!"
3. Name- Dalia Fenwick, Founder and CPO
4. Address - 482 E. Calder Avenue, Ste 2207, Tampa, FL. 33719
5. Phone - 720.555.0183

```html
<!DOCTYPE html>
<html lang="en">
<head>
<meta charset="utf-8">
<title>MARLOW Business Card</title>
<link href="https://fonts.googleapis.com/css2?family=Arimo:ital,wght@0,400;0,700;1,400&display=swap" rel="stylesheet">
<style>
  :root {
    --backdrop: #e4e4e2;
    --card-light: #f7f7f6;
    --card-dark: #2b2b2b;
    --card-dark-deep: #1d1d1d;
    --ink: #1f1f1f;
    --ink-soft: #6e6e6e;
    --paper-white: #ffffff;
    --paper-muted: #b9b9b9;
    --rule: #8a8a8a;
  }
  * { margin: 0; padding: 0; box-sizing: border-box; }
  html, body {
    width: 1200px;
    height: 801px;
    overflow: hidden;
    background: var(--backdrop);
    font-family: "Arimo", Arial, sans-serif;
  }
  .stage {
    position: relative;
    width: 1200px;
    height: 801px;
    display: flex;
    align-items: center;
    justify-content: center;
    gap: 60px;
  }
  .card {
    position: relative;
    width: 525px;
    height: 300px;
    box-shadow: 0 10px 24px rgba(0,0,0,0.14);
    overflow: hidden;
  }

  /* Front */
  .card--front { background: var(--card-light); color: var(--ink); }
  .brand {
    position: absolute;
    left: 0;
    right: 0;
    top: 78px;
    display: flex;
    align-items: center;
    justify-content: center;
    gap: 14px;
  }
  .brand__dot {
    width: 22px;
    height: 22px;
    border-radius: 50%;
    background: var(--ink);
  }
  .brand__name {
    font-weight: 700;
    font-size: 30px;
    letter-spacing: 11px;
    color: var(--ink);
  }
  .details {
    position: absolute;
    left: 0;
    right: 0;
    top: 168px;
    display: flex;
    justify-content: center;
    align-items: stretch;
    gap: 18px;
  }
  .person { text-align: right; padding-top: 14px; }
  .person__name { font-weight: 700; font-size: 19px; color: var(--ink); }
  .person__title { font-size: 16px; color: var(--ink-soft); margin-top: 2px; }
  .divider { width: 1px; background: var(--rule); }
  .contact { font-size: 14px; color: var(--ink-soft); line-height: 1.35; }
  .contact__phone {
    display: flex;
    align-items: center;
    gap: 5px;
    font-weight: 700;
    font-size: 15px;
    color: var(--ink);
    margin-bottom: 2px;
  }
  .contact__phone svg { width: 13px; height: 13px; }

  /* Back */
  .card--back {
    background: linear-gradient(135deg, var(--card-dark) 0%, var(--card-dark-deep) 100%);
  }
  .back__wordmark {
    position: absolute;
    left: 36px;
    bottom: 62px;
    font-weight: 700;
    font-size: 38px;
    letter-spacing: 20px;
    color: var(--paper-white);
  }
  .back__tagline {
    position: absolute;
    left: 38px;
    right: 30px;
    bottom: 32px;
    font-size: 14px;
    letter-spacing: 0.3px;
    color: var(--paper-muted);
  }
</style>
</head>
<body>
  <main class="stage">
    <section class="card card--front" aria-label="Card front">
      <div class="brand">
        <span class="brand__dot"></span>
        <span class="brand__name">MARLOW</span>
      </div>
      <div class="details">
        <div class="person">
          <p class="person__name">Dalia Fenwick</p>
          <p class="person__title">Founder and CPO</p>
        </div>
        <span class="divider"></span>
        <div class="contact">
          <p class="contact__phone">
            <svg viewBox="0 0 16 16" aria-hidden="true">
              <circle cx="8" cy="8" r="7" fill="none" stroke="currentColor" stroke-width="1.6"/>
              <path d="M5.2 4.6l1.4-.4.8 2-.9.7a5 5 0 0 0 2.6 2.6l.7-.9 2 .8-.4 1.4c-3.4.3-6.5-2.8-6.2-6.2z" fill="currentColor"/>
            </svg>
            720.555.0183
          </p>
          <p>482 E. Calder Avenue</p>
          <p>Ste 2207, Tampa, FL. 33719</p>
        </div>
      </div>
    </section>

    <section class="card card--back" aria-label="Card back">
      <p class="back__wordmark">MARLOW</p>
      <p class="back__tagline">If it keeps a drink cold or the party going...we do it!</p>
    </section>
  </main>
</body>
</html>
```